Business card design needed

we are a bakery that specialises in traditional sourdough breads all shaped by hand. we are a little rustic but cater to a wide variety of people and are based in an affluent suburb. i think i would prefer lighter earthy colours. with some dark colours like bread crust maybe.

Industry/Entity Type

Bakery

Contact Information for Business Card

MAPLEFIELD BAKERY
27 KESTREL ST
SURREY HILLS
VIC 3127
PH: 03 55501942
EMAIL: maplefield@northwire.com.au

Requirements
Must have
• no photos. hand drawing would be great

```html
<!DOCTYPE html>
<html lang="en">
<head>
<meta charset="utf-8">
<title>Maplefield Bakery – Business Card</title>
<link rel="stylesheet" href="https://fonts.googleapis.com/css2?family=Exo+2:wght@300&display=swap">
<style>
  :root {
    --backdrop: #d9d9d7;
    --card: #e7d4ae;
    --card-edge: #d8c49c;
    --ink: #ffffff;
    --gloss: rgba(255, 255, 255, 0.28);
    --gloss-soft: rgba(255, 255, 255, 0.16);
  }
  * { margin: 0; padding: 0; box-sizing: border-box; }
  html, body {
    width: 1200px;
    height: 969px;
    overflow: hidden;
    background: var(--backdrop);
  }
  .canvas {
    position: relative;
    width: 1200px;
    height: 969px;
  }
  .card {
    position: absolute;
    width: 540px;
    height: 309px;
    background: var(--card);
    border: 1px solid var(--card-edge);
    border-radius: 3px;
    overflow: hidden;
    color: var(--ink);
    font-family: "Exo 2", sans-serif;
    font-weight: 300;
    box-shadow: 0 6px 18px rgba(0, 0, 0, 0.12);
  }
  .card--front { left: 330px; top: 100px; }
  .card--back  { left: 330px; top: 540px; }

  .gloss {
    position: absolute;
    inset: 0;
    width: 100%;
    height: 100%;
    pointer-events: none;
  }

  .front-name {
    position: absolute;
    left: 60px;
    right: 0;
    top: 128px;
    text-align: center;
    font-size: 32px;
    font-weight: 300;
    letter-spacing: 1px;
  }

  .back-name {
    position: absolute;
    left: 44px;
    top: 118px;
    font-size: 21px;
    font-weight: 300;
    letter-spacing: 0.5px;
  }
  .divider {
    position: absolute;
    left: 268px;
    top: 104px;
    width: 1px;
    height: 78px;
    background: var(--ink);
  }
  .contact {
    position: absolute;
    left: 288px;
    top: 126px;
    list-style: none;
    font-size: 12px;
    letter-spacing: 0.5px;
  }
  .contact li {
    display: flex;
    align-items: center;
    gap: 12px;
    height: 22px;
  }
  .contact svg { width: 11px; height: 11px; flex: none; }
  .contact .email { text-transform: uppercase; font-size: 10.5px; }
  .address {
    position: absolute;
    left: 176px;
    top: 206px;
    width: 200px;
    text-align: center;
    font-style: normal;
    font-size: 10.5px;
    line-height: 16px;
    letter-spacing: 0.3px;
    text-transform: uppercase;
  }
</style>
</head>
<body>
<main class="canvas">

  <section class="card card--front" aria-label="Business card front">
    <svg class="gloss" viewBox="0 0 540 309" aria-hidden="true">
      <polygon points="0,60 40,60 150,309 110,309" fill="var(--gloss)"/>
      <polygon points="60,150 120,150 190,309 130,309" fill="var(--gloss-soft)"/>
    </svg>
    <p class="front-name">Maplefield Bakery</p>
  </section>

  <section class="card card--back" aria-label="Business card back">
    <svg class="gloss" viewBox="0 0 540 309" aria-hidden="true">
      <polygon points="0,110 30,110 120,309 90,309" fill="var(--gloss)"/>
      <polygon points="50,160 110,160 175,309 115,309" fill="var(--gloss-soft)"/>
    </svg>
    <h1 class="back-name">Maplefield Bakery</h1>
    <span class="divider" aria-hidden="true"></span>
    <ul class="contact">
      <li>
        <svg viewBox="0 0 24 24" aria-hidden="true"><path fill="#fff" d="M6.6 10.8a15.2 15.2 0 0 0 6.6 6.6l2.2-2.2a1 1 0 0 1 1-.25 11.4 11.4 0 0 0 3.6.57 1 1 0 0 1 1 1V20a1 1 0 0 1-1 1A17 17 0 0 1 3 4a1 1 0 0 1 1-1h3.5a1 1 0 0 1 1 1c0 1.25.2 2.450.57 3.57a1 1 0 0 1-.25 1z"/></svg>
        <span class="phone">03 55501942</span>
      </li>
      <li>
        <svg viewBox="0 0 24 24" aria-hidden="true"><path fill="#fff" d="M2 5h20v14H2zm2 2v.5l8 5 8-5V7z"/></svg>
        <span class="email">maplefield@northwire.com.au</span>
      </li>
    </ul>
    <address class="address">27 Kestrel St<br>Alderwood Vale, QLD 4599</address>
  </section>

</main>
</body>
</html>
```